Spray Foam Company Business Card

We need a business card designed for our spray foam insulation and roof coatings business. We handle residential and commercial projects.
Industry/Entity Type
Construction
Contact Information for Business Card
We would like it to say:
K & R Coat
with these bullet points
-foam insulation
-waterproofing roof system
-water proofing foundation systems
website is krcoatfoamsealers.com (this was just purchased)
office phone : 630-555-0148
And 3 cards with names on them the names are :
Darren Hollis
Trevor Lindqvist
Neil Bruxton
maybe the bullet points can go on the back?
if you go this website it is another division of our company and you can see the font we use in the K & R. We do not want to use the same half circles that it has just the lettering
www.thesturdiestfinishwork.com
Look and feel
Each slider illustrates characteristics of the customer's brand and the style your logo design should communicate.

```html
<!DOCTYPE html>
<html lang="en">
<head>
<meta charset="utf-8">
<title>K &amp; R Coat — Business Card</title>
<link rel="stylesheet" href="https://fonts.googleapis.com/css2?family=PT+Sans:wght@400;700&family=Arimo:ital@1&display=swap">
<style>
  :root {
    --navy: #2a2e6e;
    --green: #6db045;
    --paper: #ffffff;
    --ink: #3a3a3a;
    --ink-soft: #444444;
    --rule: #c8c8c8;
    --mark-faint: #a9a9a9;
    --backdrop: #eeeeee;
  }
  html, body { margin: 0; padding: 0; overflow: hidden; }
  .canvas {
    position: relative;
    width: 1200px;
    height: 406px;
    background: var(--backdrop);
    overflow: hidden;
  }
  .card {
    position: absolute;
    top: 69px;
    width: 468px;
    height: 267px;
    background: var(--paper);
    box-shadow: 0 1px 3px rgba(0,0,0,0.18);
    overflow: hidden;
  }
  .card--front { left: 122px; }
  .card--back  { left: 659px; }
  .card__shapes { position: absolute; inset: 0; width: 100%; height: 100%; }
  .shape-navy { fill: var(--navy); }
  .shape-green { fill: var(--green); }

  .brand-name {
    position: absolute;
    font-family: "PT Sans", sans-serif;
    font-weight: 400;
    white-space: nowrap;
    line-height: 1;
  }
  .card--front .brand-name {
    left: 0; width: 432px; text-align: center;
    top: 54px; font-size: 31px; color: var(--ink);
  }
  .card--back .brand-name {
    left: 322px; top: 216px; font-size: 29px; color: var(--mark-faint);
  }

  .person-name {
    position: absolute;
    left: 76px; top: 138px;
    font-family: "PT Sans", sans-serif;
    font-weight: 700;
    font-size: 21px;
    color: var(--ink);
    line-height: 1;
  }
  .divider-vertical {
    position: absolute;
    left: 220px; top: 115px;
    width: 2px; height: 43px;
    background: var(--rule);
  }
  .divider-horizontal {
    position: absolute;
    left: 76px; top: 175px;
    width: 322px; height: 1px;
    background: var(--rule);
  }
  .contact {
    position: absolute;
    font-family: "Arimo", sans-serif;
    font-style: italic;
    font-size: 12px;
    line-height: 16px;
    color: var(--ink-soft);
    margin: 0;
  }
  .contact--address { left: 232px; top: 116px; }
  .contact--online  { left: 88px;  top: 191px; }

  .services {
    position: absolute;
    left: 77px; top: 53px;
    margin: 0; padding: 0;
    list-style: none;
    font-family: "Arimo", sans-serif;
    font-style: italic;
    font-size: 15px;
    line-height: 20px;
    color: var(--ink);
  }
  .services li { position: relative; padding-left: 11px; }
  .services li::before {
    content: "";
    position: absolute;
    left: 0; top: 9px;
    width: 5px; height: 5px;
    border-radius: 50%;
    background: var(--navy);
  }
</style>
</head>
<body>
<main class="canvas">

  <section class="card card--front" aria-label="Business card front">
    <svg class="card__shapes" viewBox="0 0 585 334" preserveAspectRatio="none" aria-hidden="true">
      <path class="shape-navy" d="M0 0 H42 C55 140 80 250 122 334 H0 Z"/>
      <path class="shape-green" d="M462 0 H585 V334 H544 C532 200 512 90 462 0 Z"/>
    </svg>
    <div class="brand-name">K &amp; R</div>
    <div class="person-name">Darren Hollis</div>
    <div class="divider-vertical"></div>
    <p class="contact contact--address">
      218 Larkspur Lane, Millbrook,<br>
      IL 60536<br>
      Phone : 630-555-0148
    </p>
    <div class="divider-horizontal"></div>
    <p class="contact contact--online">
      Email : info@thesturdiestfinishwork.com<br>
      Website : krcoatfoamsealers.com
    </p>
  </section>

  <section class="card card--back" aria-label="Business card back">
    <svg class="card__shapes" viewBox="0 0 585 334" preserveAspectRatio="none" aria-hidden="true">
      <path class="shape-navy" d="M0 0 H42 C55 140 80 250 122 334 H0 Z"/>
      <path class="shape-green" d="M462 0 H585 V334 H544 C532 200 512 90 462 0 Z"/>
    </svg>
    <ul class="services">
      <li>foam insulation</li>
      <li>waterproofing roof system</li>
      <li>water proofing foundation systems</li>
    </ul>
    <div class="brand-name">K &amp; R</div>
  </section>

</main>
</body>
</html>
```